Business Card & Email Signature Design || Upmarket + Luxury

Riverlume Honey, a New Zealand Manuka Honey company needs a Business Card & Email Signature design.

Our logo's are attached in Gold & Black versions, feel free to be creative with how you use the logo and it's patterns in your design.

Style:
- Looking for an Elegant, Luxurious, Upmarket feel.
- Black/Matte Black Card, Gold Foil, UV Embossing

Information to Add:

- Logo
- Company Name: Riverlume Honey
- Name: Mattias Brovell
- Title: Creative Director
- Phone: +64 2919 58 617
- Email: mattias@riverlumehoney.example
- Website: www.riverlumehoney.example

- Socials: ***For email Signature Only***
- Facebook: https://www.facebook.com/riverlumehoney/
- Instagram: https://www.instagram.com/riverlumehoney/

Target Market(s)

Asia/Europe Luxury, Upmarket

Contact Information for Business Card

- Logo
- Name: Mattias Brovell
- Phone: +64 2919 58 617

Font styles to use
Other font styles liked:
• Champagne & Limousines (Attached)

Requirements
Must have
• Business Card & Email Signature Design.

Looking for a Sleek, Luxury, Upmarket Design.

```html
<!DOCTYPE html>
<html lang="en">
<head>
<meta charset="utf-8">
<title>Riverlume Honey – Business Card</title>
<link rel="stylesheet" href="https://fonts.googleapis.com/css2?family=Josefin+Sans:wght@300;400&family=Quicksand:wght@400;500&display=swap">
<style>
  :root {
    --backdrop: #1b1b1b;
    --card-black: #151515;
    --cream: #e6e4d2;
    --gold: #c9a55a;
    --gold-light: #e3c98a;
    --ink: #1a1a1a;
    --white: #f2f2f2;
  }
  * { box-sizing: border-box; margin: 0; padding: 0; }
  html, body { width: 1200px; height: 675px; overflow: hidden; }
  body {
    background: var(--backdrop);
    font-family: "Josefin Sans", sans-serif;
    position: relative;
  }
  .card {
    position: absolute;
    top: 235px;
    width: 400px;
    height: 230px;
    overflow: hidden;
    box-shadow: 0 14px 30px rgba(0,0,0,.55);
  }
  .card-bg { position: absolute; inset: 0; width: 100%; height: 100%; }
  .card-front { left: 190px; background: var(--card-black); }
  .card-back { left: 620px; background: var(--card-black); }

  /* Front */
  .brand-mark {
    position: absolute;
    left: 163px; top: 34px;
    width: 74px; height: 74px;
    border: 1.5px solid var(--gold);
    border-radius: 50%;
  }
  .brand-name {
    position: absolute;
    left: 0; right: 0; top: 122px;
    text-align: center;
    color: var(--gold);
    font-weight: 300;
    font-size: 27px;
    letter-spacing: 4px;
    text-transform: uppercase;
  }
  .website {
    position: absolute;
    left: 0; right: 0; top: 186px;
    text-align: center;
    color: var(--white);
    font-family: "Quicksand", sans-serif;
    font-weight: 500;
    font-size: 12.5px;
    letter-spacing: .3px;
  }

  /* Back */
  .stamp {
    position: absolute;
    right: 24px; top: 14px;
    width: 72px; height: 72px;
    border: 1px solid #5a5a52;
    border-radius: 50%;
    display: flex; align-items: center; justify-content: center;
    text-align: center;
    color: #3c3c36;
    font-weight: 400;
    font-size: 8px;
    letter-spacing: 1px;
    text-transform: uppercase;
    line-height: 1.3;
  }
  .job-title {
    position: absolute;
    left: 36px; top: 96px;
    font-family: "Quicksand", sans-serif;
    font-size: 12.5px;
    color: var(--ink);
    border-bottom: 1px solid var(--ink);
    padding-bottom: 1px;
  }
  .person-name {
    position: absolute;
    left: 36px; top: 118px;
    font-size: 27px;
    font-weight: 400;
    color: var(--ink);
    text-transform: uppercase;
  }
  .contact {
    position: absolute;
    left: 46px;
    list-style: none;
    top: 158px;
    font-family: "Quicksand", sans-serif;
    font-size: 12px;
    color: var(--ink);
  }
  .contact li { display: flex; align-items: center; gap: 7px; height: 20px; }
  .contact svg { width: 13px; height: 13px; flex: none; }
</style>
</head>
<body>

<section class="card card-front" aria-label="Business card front">
  <svg class="card-bg" viewBox="0 0 400 230" aria-hidden="true">
    <polygon points="0,0 50,0 0,78" fill="var(--cream)"/>
    <line x1="50" y1="0" x2="0" y2="78" stroke="var(--gold)" stroke-width="1.5"/>
    <polygon points="400,112 400,230 340,230" fill="var(--cream)"/>
    <line x1="400" y1="112" x2="340" y2="230" stroke="var(--gold)" stroke-width="1.5"/>
  </svg>
  <div class="brand-mark" aria-hidden="true"></div>
  <div class="brand-name">Riverlume Honey</div>
  <div class="website">www.riverlumehoney.example</div>
</section>

<section class="card card-back" aria-label="Business card back">
  <svg class="card-bg" viewBox="0 0 400 230" aria-hidden="true">
    <polygon points="66,0 400,0 400,80 348,230 0,230 0,112" fill="var(--cream)"/>
    <line x1="66" y1="0" x2="0" y2="112" stroke="var(--gold)" stroke-width="1.5"/>
    <line x1="400" y1="80" x2="348" y2="230" stroke="var(--gold)" stroke-width="1.5"/>
  </svg>
  <div class="stamp">Riverlume<br>Honey</div>
  <div class="job-title">Creative Director</div>
  <div class="person-name">Mattias Brovell</div>
  <ul class="contact">
    <li>
      <svg viewBox="0 0 24 24" aria-hidden="true"><path fill="var(--gold)" d="M6.6 10.8a15 15 0 0 0 6.6 6.6l2.2-2.2c.3-.3.7-.4 1-.2 1.1.4 2.3.6 3.6.6.6 0 1 .4 1 1V20c0 .6-.4 1-1 1A17 17 0 0 1 3 4c0-.6.4-1 1-1h3.5c.6 0 1 .4 1 1 0 1.3.2 2.5.6 3.6.1.3 0 .7-.2 1z"/></svg>
      <span>+64 2919 58 617</span>
    </li>
    <li>
      <svg viewBox="0 0 24 24" aria-hidden="true"><rect x="2" y="5" width="20" height="14" fill="none" stroke="var(--gold)" stroke-width="2"/><polyline points="2,5 12,13 22,5" fill="none" stroke="var(--gold)" stroke-width="2"/></svg>
      <span>mattias@riverlumehoney.example</span>
    </li>
  </ul>
</section>

</body>
</html>
```